Fun, Clean Business Card For Family Focused Travel Agency

I need a business card using specific colors and fonts as in the uploaded files. Ideally, I would like a large image of the logo on the back and all the contact info on the front. Maybe the stars/dots somewhere in a flowy form.

I do want it the contact information to be clear and easy to read. I don't want it to look too busy. Maybe even a bit minimalist.

I plan or ordering the ROUNDED CORNER business cards from Cardwell Press, so please consider that in your design.

Target Market(s)

Families with children, couples, groups of friends

Contact Information for Business Card

Marla Quent, Owner
Marla@TidewayTrips.example
Cell Phone Number 555-218-6034
Office Phone Number 555-647-1295
Specializing in Fablecrest destinations, Goldmere Parkside Resort, Cruises and All-Inclusive Vacations.

Nice but not required:
www.TidewayTrips.example
Facebook, Instagram, Twitter icons with username: TidewayTrips

Font styles to use
Sans Serif

Requirements
Must have
• Please try to use the colors from the logo as much as possible. I understand lighter shades/colors may be needed for some things.
Should not have
• NO SERIF FONTS. That is really the only thing I do not want at all

```html
<!DOCTYPE html>
<html lang="en">
<head>
<meta charset="utf-8">
<title>Tideway Trips – Business Card</title>
<link href="https://fonts.googleapis.com/css2?family=Ubuntu:wght@300;400;700&display=swap" rel="stylesheet">
<style>
  :root {
    --bg: #eceae6;
    --teal: #22b59a;
    --teal-deep: #1a9d85;
    --silver: #e4e8ea;
    --ink: #2b2d3a;
    --white: #ffffff;
    --star-orange: #f08a24;
    --star-blue: #3a8fd8;
    --star-yellow: #f2c230;
    --faint: #eef0f1;
  }
  * { box-sizing: border-box; margin: 0; padding: 0; }
  html, body { width: 1200px; height: 800px; overflow: hidden; }
  body {
    background: var(--bg);
    font-family: "Ubuntu", Arial, sans-serif;
    color: var(--ink);
    position: relative;
  }
  .card {
    position: absolute;
    top: 245px;
    width: 540px;
    height: 309px;
    border-radius: 26px;
    overflow: hidden;
    box-shadow: 0 6px 18px rgba(0,0,0,0.12);
  }
  /* Logo side */
  .card-logo-side { left: 40px; background: var(--teal); }
  .card-logo-side .brand-art {
    position: absolute; left: 120px; top: 70px;
    width: 120px; height: 110px; border-radius: 50%;
    background: radial-gradient(circle at 45% 45%, #f4f6f7, #b9c2c6);
  }
  .card-logo-side .brand-name {
    position: absolute; left: 250px; top: 100px;
    font-size: 40px; font-weight: 400; color: var(--silver);
    letter-spacing: 0.5px;
  }
  .specialty {
    position: absolute; left: 0; right: 0; top: 214px; text-align: center;
  }
  .specialty-heading { font-size: 13px; font-weight: 700; color: var(--ink); margin-bottom: 14px; }
  .specialty-list { font-size: 11.5px; color: var(--white); white-space: nowrap; }
  .specialty-list .star { font-size: 11px; margin: 0 2px 0 6px; }
  .star.orange { color: var(--star-orange); }
  .star.blue { color: var(--star-blue); }
  .star.yellow { color: var(--star-yellow); }

  /* Contact side */
  .card-contact-side { left: 620px; background: var(--white); }
  .card-contact-side .brand-watermark {
    position: absolute; left: 30px; top: 150px;
    width: 260px; height: 220px; border-radius: 50%;
    background: radial-gradient(circle, var(--faint), rgba(238,240,241,0));
  }
  .contact {
    position: absolute; left: 270px; top: 34px;
  }
  .contact-name { font-size: 22px; font-weight: 700; color: var(--ink); line-height: 1.1; }
  .contact-title { font-size: 22px; font-weight: 300; color: var(--teal); margin-bottom: 20px; }
  .contact-line {
    display: flex; align-items: center; gap: 9px;
    font-size: 13px; color: var(--ink); margin-bottom: 8px;
  }
  .contact-line svg { width: 13px; height: 13px; flex: none; }
  .contact-social { margin-top: 14px; }
  .social-square { width: 12px; height: 12px; background: var(--teal); border-radius: 2px; flex: none; }
  .contact-web { font-size: 13px; color: var(--teal); margin-top: 4px; padding-left: 21px; }
  .card-contact-side .brand-art {
    position: absolute; left: 60px; top: 200px;
    width: 80px; height: 72px; border-radius: 50%;
    background: radial-gradient(circle at 45% 45%, #8fd3c4, #2b2d3a);
  }
  .card-contact-side .brand-name {
    position: absolute; left: 150px; top: 214px;
    font-size: 36px; font-weight: 400; color: var(--ink);
  }
</style>
</head>
<body>
  <section class="card card-logo-side">
    <div class="brand-art" role="img" aria-label="Sailing ship illustration with scattered stars and dots"></div>
    <div class="brand-name">Tideway Trips</div>
    <div class="specialty">
      <p class="specialty-heading">Specializing in</p>
      <p class="specialty-list"><span class="star yellow">★</span>Fablecrest destinations<span class="star blue">★</span>Goldmere Parkside Resort<span class="star orange">★</span>Cruises and All-Inclusive Vacations</p>
    </div>
  </section>

  <section class="card card-contact-side">
    <div class="brand-watermark" role="img" aria-label="Faint large ship illustration behind the logo"></div>
    <div class="contact">
      <p class="contact-name">Marla Quent</p>
      <p class="contact-title">Owner</p>
      <p class="contact-line">
        <svg viewBox="0 0 14 14"><rect x="3.5" y="1" width="7" height="12" rx="1.5" fill="none" stroke="#22b59a" stroke-width="1.4"/><circle cx="7" cy="11" r="0.8" fill="#22b59a"/></svg>
        555-218-6034
      </p>
      <p class="contact-line">
        <svg viewBox="0 0 14 14"><path d="M1 5c2-3 10-3 12 0l-2 2-2-1V4.5H5V6L3 7z" fill="#22b59a"/><rect x="3" y="7.5" width="8" height="5" rx="1" fill="#22b59a"/></svg>
        555-647-1295
      </p>
      <p class="contact-line">
        <svg viewBox="0 0 14 14"><rect x="1" y="3" width="12" height="8.5" fill="#22b59a"/><path d="M1 3l6 5 6-5" fill="none" stroke="#fff" stroke-width="1.1"/></svg>
        Marla@TidewayTrips.example
      </p>
      <p class="contact-line contact-social"><span class="social-square"></span>TidewayTrips</p>
      <p class="contact-web">www.TidewayTrips.example</p>
    </div>
    <div class="brand-art" role="img" aria-label="Colourful sailing ship illustration with stars and dots"></div>
    <div class="brand-name">Tideway Trips</div>
  </section>
</body>
</html>
```